Geschäftspapiere für unternehmerische Holding für Beteiligungen, Projektgesellschaften und kaufmännische Steuerung
Zielgruppe
Die Hollwen GmbH ist eine unternehmerische Holding für Beteiligungen, Projektgesellschaften und kaufmännische Steuerung. Sie übernimmt Management-, Controlling- und Strukturierungsaufgaben für verbundene Unternehmen.
Zielgruppe sind Banken, Investoren, Geschäftspartner, Steuerberater, Rechtsanwälte, Behörden sowie Geschäftsführungen und Gesellschafter von Beteiligungs- und Projektgesellschaften.
Aufgabenstellung
Gesucht wird ein digitales Briefpapier für die Hollwen GmbH, das sowohl als PDF/Dokumentvorlage als auch beim Ausdruck professionell funktioniert.
Wichtig ist ein sehr klarer, hochwertiger und seriöser Auftritt. Das Design soll reduziert, strukturiert und geschäftlich wirken – keine verspielten Elemente, keine überladenen Grafiken, keine auffälligen Muster.
Das Briefpapier muss drucktauglich sein. Bitte ausreichende Druckränder und Sicherheitsabstände berücksichtigen, damit Kopf- und Fußbereich auch auf normalen Büro- und Laserdruckern sauber ausgegeben werden können. Das Layout soll sowohl digital als auch gedruckt stimmig aussehen.
Format: DIN A4 Hochformat.
Gewünschte Inhalte:
* Logo der Hollwen GmbH
* Firmenname: Hollwen GmbH
* Geschäftsanschrift: Lindauer Weg 52, 80339 München
* Telefon: 089 58210946
* E-Mail: info@hollwenbeta.example
* Webseite: hollwenbeta.example
* Geschäftsführung: Dipl.-Wirtschaftsing. (FH) Till Osterwald
* Registergericht / Amtsgericht München HRB 527081
* Bankverbindung IBAN DE918204 5571 0009 1826 40
Besonderer Wert liegt auf:
* hochwertiger Holding-/Investment-Anmutung
* sehr guter Lesbarkeit
* klarer Kopf- und Fußzeile
* sauberer Typografie
* professioneller Nutzbarkeit für Angebote, Verträge, Behörden- und Bankkorrespondenz
Bitte das Design so anlegen, dass es später als editierbare Word-/PDF-Vorlage genutzt werden kann und sowohl das Logo, als auch die Farben entsprechend verwenden.

```html
<!DOCTYPE html>
<html lang="de">
<head>
<meta charset="utf-8">
<title>Hollwen GmbH – Briefpapier</title>
<link rel="stylesheet" href="https://fonts.googleapis.com/css2?family=Montserrat:wght@300;400;600&display=swap">
<style>
  :root {
    --navy: #121c34;
    --silver: #b9bcc2;
    --ink: #2a2f3a;
    --muted: #5a6070;
    --backdrop: #ebebeb;
    --paper: #ffffff;
  }
  * { box-sizing: border-box; margin: 0; padding: 0; }
  html, body { width: 1200px; height: 960px; overflow: hidden; }
  body {
    background: var(--backdrop);
    font-family: "Montserrat", sans-serif;
    color: var(--ink);
    position: relative;
  }
  .letter {
    position: absolute;
    left: 282px; top: 30px;
    width: 636px; height: 900px;
    background: var(--paper);
    box-shadow: 0 2px 10px rgba(0,0,0,0.12);
    overflow: hidden;
  }
  .letter-head {
    position: absolute; left: 0; top: 0;
    width: 100%; height: 172px;
    background: var(--navy);
  }
  .brand-name {
    position: absolute; left: 74px; top: 100px;
    font-weight: 300; font-size: 34px;
    letter-spacing: 9px; text-transform: uppercase;
    color: var(--silver);
  }
  .sender-line {
    position: absolute; left: 74px; top: 198px;
    font-size: 6.5px; color: var(--ink);
  }
  .sender-line strong { font-weight: 600; }
  .fold-mark {
    position: absolute; left: 0; width: 16px; height: 1px;
    background: #9a9ea6;
  }
  .fold-mark.upper { top: 298px; }
  .fold-mark.punch { top: 450px; }
  .fold-mark.lower { top: 600px; }
  .letter-body {
    position: absolute; left: 110px; top: 300px;
    width: 440px; font-size: 9.2px; line-height: 1.75;
  }
  .letter-body p { margin-bottom: 12px; text-align: justify; }
  .closing {
    position: absolute; left: 110px; top: 540px;
    font-size: 10.5px;
  }
  .signature {
    position: absolute; left: 118px; top: 562px;
    width: 150px; height: 34px;
    background: linear-gradient(90deg, rgba(18,28,52,0.10), rgba(18,28,52,0.03));
    border-radius: 3px;
  }
  .letter-foot {
    position: absolute; left: 74px; right: 40px; top: 800px;
    display: flex; align-items: flex-start; gap: 18px;
    font-size: 6.6px; line-height: 1.6; color: var(--ink);
  }
  .foot-divider { width: 1px; height: 38px; background: var(--navy); }
  .foot-address strong, .foot-legal strong { font-weight: 600; }
  .foot-contact li { list-style: none; display: flex; align-items: center; gap: 6px; }
  .foot-contact svg { width: 7px; height: 7px; fill: var(--navy); }
  .letter-base {
    position: absolute; left: 0; bottom: 0;
    width: 100%; height: 14px; background: var(--navy);
  }
</style>
</head>
<body>
  <article class="letter">
    <header class="letter-head">
      <div class="brand-name">Hollwen</div>
    </header>

    <div class="sender-line"><strong>Hollwen GmbH |</strong> Lindauer Weg 52 | 80339 München</div>

    <span class="fold-mark upper"></span>
    <span class="fold-mark punch"></span>
    <span class="fold-mark lower"></span>

    <section class="letter-body">
      <p>Sehr geehrte Damen und Herren,</p>
      <p>Blindtexte nennt man Texte, die bei der Produktion von Publikationen oder Webseiten als Platzhalter für spätere Inhalte stehen, wenn der eigentliche Text noch nicht vorhanden ist. Sie werden auch als Dummy-, Füll- oder Platzhaltertexte bezeichnet. Mitunter sollen Komponisten von Liedern Blindtexte beim Komponieren von Melodien benutzen und diese vor dem Dichten des Liedtextes singen.</p>
      <p>Blindtexte nennt man Texte, die bei der Produktion von Publikationen oder Webseiten als Platzhalter für spätere Inhalte stehen, wenn der eigentliche Text noch nicht vorhanden ist. Sie werden auch als Dummy-, Füll- oder Platzhaltertexte bezeichnet.</p>
    </section>

    <p class="closing">Mit freundlichen Grüßen</p>
    <div class="signature" role="img" aria-label="Handschriftliche Unterschrift Max Mustermann"></div>

    <footer class="letter-foot">
      <div class="foot-address">
        <strong>Hollwen GmbH</strong><br>
        Lindauer Weg 52<br>
        80339 München
      </div>
      <span class="foot-divider"></span>
      <ul class="foot-contact">
        <li><svg viewBox="0 0 10 10"><path d="M2 0.5 L3.8 2.6 L2.9 3.8 Q4 6 6.2 7.1 L7.4 6.2 L9.5 8 L8.3 9.5 Q1 8 0.5 1.7 Z"/></svg>089 58210946</li>
        <li><svg viewBox="0 0 10 10"><path d="M0 2 H10 V8.5 H0 Z M0.6 2.4 L5 5.6 L9.4 2.4" stroke="#fff" stroke-width="0.7"/></svg>info@hollwenbeta.example</li>
        <li><svg viewBox="0 0 10 10"><circle cx="5" cy="5" r="4.5"/><path d="M0.5 5 H9.5 M5 0.5 V9.5" stroke="#fff" stroke-width="0.6"/></svg>www.hollwenbeta.example</li>
      </ul>
      <span class="foot-divider"></span>
      <div class="foot-legal">
        <strong>Geschäftsführung:</strong> Dipl.-Wirtschaftsing. (FH) Till Osterwald<br>
        Amtsgericht München HRB 527081<br>
        Bankverbindung IBAN DE918204 5571 0009 1826 40
      </div>
    </footer>

    <div class="letter-base"></div>
  </article>
</body>
</html>
```